Lantern Trails of Hollowmere Valley Tour Flyer

I need a one page flyer, one sided, full color. The main part of the flyer should be ONLY ONE of the attached photos. All text is included with SAMPLE/EXAMPLE sizing, but actual sizing and placement, and FONT are up to you. Font should be clear and legible, and one font should be used for all titles/larger text, and another for all small/paragraph text.

```html
<!DOCTYPE html>
<html lang="en">
<head>
<meta charset="utf-8">
<title>Lantern Trails of Hollowmere Valley Tour Flyer</title>
<link href="https://fonts.googleapis.com/css2?family=Roboto+Condensed:wght@300;400;700&family=Raleway:wght@400;500;700&display=swap" rel="stylesheet">
<style>
  :root {
    --backdrop: #b9b9bd;
    --flyer-dark: #161616;
    --flyer-mid: #3a3a3a;
    --flyer-light: #5a5a5a;
    --band: #101010;
    --text-main: #f2f2f2;
    --text-soft: #d6d6d6;
    --text-dim: #a4a4a4;
    --photo-top: #4a4a4c;
    --photo-mid: #2a2a2c;
    --photo-bottom: #111112;
  }
  * { margin: 0; padding: 0; box-sizing: border-box; }
  html, body {
    width: 1200px; height: 1000px; overflow: hidden;
    background: var(--backdrop);
  }
  .flyer {
    position: absolute; left: 80px; top: 60px;
    width: 1040px; height: 880px; overflow: hidden;
    background:
      radial-gradient(ellipse 620px 520px at 780px 260px, var(--flyer-light), transparent 70%),
      linear-gradient(160deg, var(--flyer-mid) 0%, #262626 45%, var(--flyer-dark) 100%);
    box-shadow: 0 14px 34px rgba(0,0,0,0.35);
    color: var(--text-main);
  }
  .flyer > * { position: absolute; z-index: 1; }
  .photo {
    z-index: 0 !important;
    left: 590px; top: 200px; width: 410px; height: 570px;
    background: linear-gradient(180deg, var(--photo-top) 0%, var(--photo-mid) 55%, var(--photo-bottom) 100%);
  }
  .headline {
    left: 58px; top: 58px;
    font-family: "Roboto Condensed", sans-serif;
    font-size: 66px; line-height: 0.95; text-transform: uppercase;
    letter-spacing: 0.5px; white-space: nowrap;
  }
  .headline b { font-weight: 700; }
  .headline span { font-weight: 300; }
  .presenter {
    left: 230px; top: 272px; width: 330px;
    text-align: right; font-family: "Roboto Condensed", sans-serif;
    text-transform: uppercase; white-space: nowrap;
  }
  .presenter .lead { font-weight: 700; font-size: 26px; line-height: 1; }
  .presenter .act { font-weight: 300; font-size: 24px; line-height: 1.1; }
  .intro {
    left: 130px; top: 365px; width: 440px;
    font-family: "Raleway", sans-serif; font-variant: small-caps;
    font-size: 15px; line-height: 1.32; letter-spacing: 0.4px;
    color: var(--text-soft);
  }
  .intro strong { color: var(--text-main); font-weight: 700; }
  .tagline {
    left: 290px; top: 590px; width: 540px;
    text-align: center; font-family: "Roboto Condensed", sans-serif;
    font-weight: 700; font-size: 27px; line-height: 1.05;
    text-transform: uppercase; white-space: nowrap;
  }
  .band {
    left: 0; top: 770px; width: 1040px; height: 110px;
    background: linear-gradient(180deg, #1c1c1c, var(--band));
  }
  .bio {
    position: absolute; left: 130px; top: 14px; width: 520px;
    font-family: "Raleway", sans-serif; font-variant: small-caps;
    font-size: 12px; line-height: 1.3; letter-spacing: 0.3px;
    color: var(--text-dim);
  }
  .quote {
    width: 270px; text-align: right;
    font-family: "Raleway", sans-serif; font-variant: small-caps;
    font-size: 15px; line-height: 1.15; color: var(--text-soft);
  }
  .quote cite {
    display: block; font-style: normal; font-family: "Roboto Condensed", sans-serif;
    font-weight: 700; font-size: 12px; text-transform: uppercase; color: var(--text-main);
    margin-top: 2px;
  }
  .quote.first { left: 740px; top: 728px; z-index: 2; }
  .quote.second { left: 740px; top: 800px; z-index: 2; }
</style>
</head>
<body>
  <main class="flyer">
    <div class="photo" role="img" aria-label="Portrait photograph of the lead singer in a dark suit jacket and open-collar shirt"></div>

    <h1 class="headline">
      <b>Lantern Trails</b><br>
      <span>Of</span> <b>Hollowmere</b><br>
      <b>Valley</b> <span>Tour.</span>
    </h1>

    <div class="presenter">
      <div class="lead">With the</div>
      <div class="act">Corin Vale Trio</div>
    </div>

    <p class="intro">
      The world's most beloved melodies in ten languages featuring songs like
      <strong>"Willow Road"</strong>, <strong>"Le Ciel d'Ambre"</strong>,
      <strong>"Luna de Plata"</strong>, <strong>"River Under Quiet Stars"</strong>, and more!
      Original arrangements by an Aurora-winning composer tap into the rare talent of
      countertenor Corin Vale, and his soloist collaborators, an outstanding Ashford-trained
      concert pianist, and a wind soloist from the Eastport Philharmonic on oboe,
      english horn, flute, and clarinet.
    </p>

    <p class="tagline">The world's favorite melodies<br>like you've never heard them before!</p>

    <section class="band">
      <p class="bio">
        Corin Vale has performed around the world from Marlow Hall to Vienna's Ardent Hall
        using extraordinary vocal range, versatility, and a hilarious rapport with the audience
        to entertain. A full time member of the Meridian-winning ensemble Brightwater, his voice
        can be heard on every major record label with a range of artists from Sela Monroe to
        the Harbor Philharmonic.
      </p>
    </section>

    <blockquote class="quote first">"Vale has Star Quality"<cite>- Riverside Courier</cite></blockquote>
    <blockquote class="quote second">"Performances of<br>Great Vitality and Verve"<cite>- Coastline Times</cite></blockquote>
  </main>
</body>
</html>
```